" A clínica já existe há 15 anos, atendendo a classe "C". Já possui uma logo há 8 anos. Este serviço solicitado será para uma nova sede que atenderá o público "A". O produto principal desta nova clínica é o aparelho estético (invisível). "

```html
<!DOCTYPE html>
<html lang="pt-BR">
<head>
<meta charset="UTF-8">
<title>Papel timbrado – Helena Vasconi Ortodontia Invisível</title>
<link rel="stylesheet" href="https://fonts.googleapis.com/css2?family=Montserrat:wght@300;400;500&display=swap">
<style>
  :root {
    --backdrop: #d9d9d9;
    --paper: #ffffff;
    --ink: #2b2b2b;
    --ink-soft: #6a6a6a;
    --band-black: #111111;
    --band-grey: #8a8a8a;
    --band-grey-light: #cfcfcf;
  }
  html, body {
    margin: 0;
    padding: 0;
    width: 1200px;
    height: 1200px;
    overflow: hidden;
    background: var(--backdrop);
    font-family: "Montserrat", Arial, sans-serif;
  }
  .letterhead {
    position: absolute;
    left: 247px;
    top: 50px;
    width: 705px;
    height: 1100px;
    background: var(--paper);
    overflow: hidden;
  }
  .top-tab {
    position: absolute;
    top: 0;
    left: 50%;
    transform: translateX(-50%);
    width: 265px;
    height: 12px;
    background: var(--band-black);
  }
  .brand {
    position: absolute;
    top: 128px;
    left: 0;
    right: 0;
    text-align: center;
    color: var(--ink);
  }
  .brand-name {
    font-size: 36px;
    font-weight: 400;
    letter-spacing: 1px;
    text-transform: uppercase;
    line-height: 1;
  }
  .brand-tagline {
    margin-top: 10px;
    font-size: 13px;
    font-weight: 400;
    letter-spacing: 4px;
    text-transform: uppercase;
    color: var(--ink-soft);
  }
  .contact {
    position: absolute;
    top: 934px;
    left: 0;
    right: 0;
    text-align: center;
    color: var(--ink-soft);
    font-size: 12.5px;
    font-weight: 400;
    line-height: 26px;
  }
  .contact .website {
    letter-spacing: 3px;
  }
  .footer-band {
    position: absolute;
    left: 0;
    bottom: 0;
    width: 705px;
    height: 95px;
    display: block;
  }
</style>
</head>
<body>
  <main class="letterhead">
    <div class="top-tab"></div>

    <header class="brand">
      <div class="brand-name">Helena Vasconi</div>
      <div class="brand-tagline">Ortodontia Invisível</div>
    </header>

    <address class="contact" style="font-style: normal;">
      <div class="phones">(51) 3210.4455 &nbsp;|&nbsp; (51) 0000.0000 / 0000.0000</div>
      <div class="street">Rua das Acácias, 120-402 - Jardim Aurora - Porto Alegre-RS</div>
      <div class="website">www.helenavasconi.com.br</div>
    </address>

    <svg class="footer-band" viewBox="0 0 705 95" preserveAspectRatio="none" aria-hidden="true">
      <defs>
        <linearGradient id="bandGrey" x1="0" y1="0" x2="1" y2="0">
          <stop offset="0" stop-color="var(--band-grey-light)"/>
          <stop offset="0.55" stop-color="var(--band-grey)"/>
          <stop offset="1" stop-color="var(--band-grey-light)"/>
        </linearGradient>
        <linearGradient id="bandBlack" x1="0" y1="0" x2="1" y2="0">
          <stop offset="0" stop-color="#000000"/>
          <stop offset="0.6" stop-color="#1c1c1c"/>
          <stop offset="1" stop-color="#3a3a3a"/>
        </linearGradient>
      </defs>
      <path class="band-grey" d="M0 42 C 220 12, 480 4, 705 14 L705 95 L0 95 Z" fill="url(#bandGrey)"/>
      <path class="band-white" d="M0 52 C 230 26, 480 22, 705 34 L705 44 C 480 34, 230 38, 0 60 Z" fill="#ffffff"/>
      <path class="band-black" d="M0 60 C 230 40, 480 40, 705 50 L705 95 L0 95 Z" fill="url(#bandBlack)"/>
    </svg>
  </main>
</body>
</html>
```